Gourmet Restaurant take out menu

We need a take out menu design that is trendy for a casual upscale Italian restaurant with a vast menu. This menu must be able to be 4 color and reproducible in large quantities to be bulked mailed or inserted into a daily paper. It must also maintain a theme that can be crossed over to our in house dining menu and specials menu.
OUR WEBSITE:
www.bellavistoplates.example
For the content, go to the Menu section of our website. We are interested in the design scheme and a template to use.
Target Market(s)
families, sinle individuals seeking take out meals and delivery
Industry/Entity Type
Restaurant
Look and feel
Each slider illustrates characteristics of the customer's brand and the style your logo design should communicate.

```html
<!DOCTYPE html>
<html lang="en">
<head>
<meta charset="utf-8">
<title>Take Out Menu</title>
<link rel="stylesheet" href="https://fonts.googleapis.com/css2?family=Noto+Serif:wght@400;700&family=Raleway:wght@300;400&display=swap">
<style>
:root{
  --paper:#dac8a2;
  --wine:#8b1a0e;
  --ink:#231a15;
  --body:#5b4b3f;
  --band-text:#f1dfc2;
  --ornament:#b57a5e;
}
*{margin:0;padding:0;box-sizing:border-box}
html,body{width:1200px;height:848px;overflow:hidden;background:var(--paper)}
.menu{position:relative;width:1200px;height:848px;background:var(--paper);color:var(--ink);font-family:"Noto Serif",serif}
.abs{position:absolute}
.rule{position:absolute;background:var(--wine);height:2px}
.vrule{position:absolute;background:var(--wine);width:2px}
.dash{position:absolute;height:2px;background:repeating-linear-gradient(90deg,var(--wine) 0 12px,transparent 12px 19px)}
.section-title{position:absolute;font-family:"Noto Serif",serif;font-weight:700;font-size:32px;letter-spacing:.5px;white-space:nowrap;transform:translate(-50%,-50%);color:var(--ink)}
.item{position:absolute;display:flex;justify-content:space-between;align-items:baseline;transform:translateY(-50%)}
.item-name{font-family:"Noto Serif",serif;font-weight:700;font-size:15px;letter-spacing:.3px;text-transform:uppercase}
.item-price{font-family:"Noto Serif",serif;font-size:9.5px}
.item-desc{position:absolute;font-family:"Raleway",sans-serif;font-weight:300;font-size:10.4px;line-height:12.8px;color:var(--body);transform:translateY(-6.4px)}
.col-left{left:49px;width:323px}
.col-mid{left:428px;width:346px}
.col-right{left:829px;width:322px}
.band{position:absolute;background:var(--wine);height:25px}
.band .item{top:12.5px;color:var(--band-text)}
.band .item-name{font-weight:700}
.toppings-title{position:absolute;left:207px;top:130px;transform:translate(-50%,-50%);font-size:16px;white-space:nowrap}
.toppings{position:absolute;left:104px;top:160px;font-family:"Raleway",sans-serif;font-size:12.5px;line-height:24.6px;color:var(--ink);white-space:nowrap}
.ornament{position:absolute;background:linear-gradient(180deg,rgba(181,122,94,.15),rgba(139,26,14,.35),rgba(181,122,94,.15));border-radius:10px}
.small-table{position:absolute;font-family:"Noto Serif",serif;font-weight:700;font-size:7.4px}
.small-table .r{display:flex;justify-content:space-between;height:14.4px;line-height:14.4px}
.lunch-sub{position:absolute;left:603px;top:512px;transform:translate(-50%,-50%);font-size:8px;white-space:nowrap;letter-spacing:.2px}
.bev{position:absolute;font-family:"Raleway",sans-serif;font-size:8.6px;line-height:10.2px;text-align:center;color:var(--ink);transform:translateX(-50%);white-space:nowrap}
.bev-price{position:absolute;font-size:9.5px;transform:translate(-50%,-50%)}
</style>
</head>
<body>
<main class="menu">
  <!-- frame rules -->
  <div class="rule" style="left:0;top:21px;width:818px"></div>
  <div class="rule" style="left:400px;top:52px;width:374px"></div>
  <div class="vrule" style="left:400px;top:52px;height:796px"></div>
  <div class="vrule" style="left:800px;top:96px;height:712px"></div>
  <div class="rule" style="left:428px;top:806px;width:374px"></div>
  <div class="rule" style="left:800px;top:99px;width:366px"></div>

  <!-- Pizza column -->
  <h1 class="section-title" style="left:210px;top:72px">GOURMENT PIZZA</h1>
  <div class="rule" style="left:48px;top:97px;width:140px"></div>
  <div class="rule" style="left:240px;top:97px;width:132px"></div>
  <div class="toppings-title">Toppings for 1.99</div>
  <div class="ornament" role="img" aria-label="Decorative scroll flourish" style="left:50px;top:178px;width:20px;height:132px"></div>
  <div class="ornament" role="img" aria-label="Decorative scroll flourish" style="left:350px;top:178px;width:20px;height:132px"></div>
  <div class="toppings">
    HAM • BROCCOLI • EXTRA CHEESE<br>
    TOMATOES HOT OR SWEET PEPPERS<br>
    • ROASTED PEPPERS • PEPPERONI •<br>
    SPINACH • ITALIAN SAUSAGE • ONIONS<br>
    • BLACK OLIVES • GREEN PEPPERS •<br>
    MUSHROOMS • GRILLED CHICKEN<br>
    MEATBALL BACON and RICOTTA 3.00
  </div>

  <div class="item col-left" style="top:354px"><span class="item-name">Plain Cheese</span><span class="item-price">8.99/11.99/12.99</span></div>
  <div class="item col-left" style="top:387px"><span class="item-name">Traditional White</span><span class="item-price">8.59/11.59/13.99</span></div>
  <p class="item-desc col-left" style="top:408px">Olive oil, garlic, mozzarella cheese</p>
  <div class="item col-left" style="top:441px"><span class="item-name">Chicken Bacon Ranch</span><span class="item-price">10.99/14.99/16.99</span></div>
  <p class="item-desc col-left" style="top:463px">Garlic chicken, bacon, pepperjack &nbsp;and cheddar cheese,<br>red onions, diced tomatoes, drizzle of ranch dressing</p>
  <div class="item col-left" style="top:510px"><span class="item-name">Bronx Bomber</span><span class="item-price">11.99/14.99/16.99</span></div>
  <p class="item-desc col-left" style="top:533px">Sausage, prosciutto ham, oregano, crumbled bleu and mozzarella<br>cheese</p>
  <div class="item col-left" style="top:585px"><span class="item-name">Buffalo Chicken</span><span class="item-price">10.99/14.99/16.99</span></div>
  <p class="item-desc col-left" style="top:612px">Buffalo sauce, chicken, mozzarella cheese, side of bleu cheese<br>dressing</p>
  <div class="band" style="left:37px;top:645px;width:363px">
    <div class="item" style="left:11px;width:335px"><span class="item-name">Gourment Special</span><span class="item-price">12.99/16.99/18.99</span></div>
  </div>
  <p class="item-desc col-left" style="top:683px">Buffalo sauce, chicken, mozzarella cheese, side of bleu cheese<br>dressing</p>
  <div class="item col-left" style="top:729px"><span class="item-name">Margarita</span><span class="item-price">8.99/11.99/13.99</span></div>
  <p class="item-desc col-left" style="top:752px">Fresh basil, tomato, buffalo mozzarella cheese</p>
  <div class="dash" style="left:168px;top:779px;width:76px"></div>
  <div class="rule" style="left:37px;top:806px;width:335px"></div>

  <!-- Middle column -->
  <div class="item col-mid" style="top:95px"><span class="item-name">Roasted Vegetable</span><span class="item-price">11.99/14.99/16.99</span></div>
  <p class="item-desc col-mid" style="top:119px">Eggplant, red and yellow peppers, onions, artichokes, Kalamata olives,<br>tomatoes, mozzarella cheese. Veggie Lover Olive oil, garlic, broccoli,<br>spinach, tomato, mozzarella cheese</p>
  <div class="band" style="left:400px;top:166px;width:384px">
    <div class="item" style="left:27px;width:347px"><span class="item-name">Sweet Hawaiian</span><span class="item-price">11.99/14.99/16.99</span></div>
  </div>
  <p class="item-desc col-mid" style="top:203px">Pineapple, tomatoes, ham, mozzarella cheese</p>
  <div class="item col-mid" style="top:240px"><span class="item-name">Spinach and Artichoke</span><span class="item-price">8.99/11.99/12.99</span></div>
  <p class="item-desc col-mid" style="top:265px">Spinach, artichoke hearts, basil, mozzarella, parmesan cheese</p>
  <div class="item col-mid" style="top:307px"><span class="item-name">Philly Chease Steak</span><span class="item-price">11.99/14.99/16.99</span></div>
  <p class="item-desc col-mid" style="top:329px">Philly steak, green peppers, onions, provolone, American cheese.</p>
  <div class="item col-mid" style="top:374px"><span class="item-name">Grandma`s Pie</span><span class="item-price">14.99</span></div>
  <p class="item-desc col-mid" style="top:401px">Thin crust pizza topped with mozzarella,<br>tomato sauce, buffalo mozzarella, fresh basil, olive oil. (One Size)</p>

  <h2 class="section-title" style="left:598px;top:468px">LUNCH ABILITIES</h2>
  <div class="rule" style="left:436px;top:492px;width:130px"></div>
  <div class="rule" style="left:632px;top:492px;width:134px"></div>
  <div class="lunch-sub">A SMALLER PORTION OF SOME OF YOUR GOURMET FAVORITES</div>
  <div class="small-table" style="left:428px;top:540px;width:159px">
    <div class="r"><span>Baked Penne Pasta</span><span>7.99</span></div>
    <div class="r"><span>Chicken Parmigiana</span><span>8.99</span></div>
    <div class="r"><span>Chicken Rosa</span><span>8.99</span></div>
    <div class="r"><span>Eggplant Parmigiana</span><span>8.99</span></div>
    <div class="r"><span>Chicken Francaise</span><span>8.99</span></div>
  </div>
  <div class="vrule" style="left:599px;top:524px;height:100px;width:1.5px"></div>
  <div class="small-table" style="left:614px;top:540px;width:160px">
    <div class="r"><span>Penne Italiano</span><span>8.99</span></div>
    <div class="r"><span>Linguini and Clams</span><span>8.99</span></div>
    <div class="r"><span>Add a House Salad or</span><span></span></div>
    <div class="r"><span>Cup of Soup Du Jour</span><span>2.99</span></div>
  </div>
  <div class="rule" style="left:428px;top:624px;width:346px"></div>

  <h2 class="section-title" style="left:598px;top:654px">BEVERAGES</h2>
  <div class="dash" style="left:428px;top:664px;width:76px"></div>
  <div class="dash" style="left:696px;top:664px;width:76px"></div>
  <div class="dash" style="left:400px;top:737px;width:94px;background:repeating-linear-gradient(90deg,var(--wine) 0 24px,transparent 24px 38px)"></div>
  <span class="bev-price" style="left:482px;top:700px">1.99</span>
  <span class="bev-price" style="left:730px;top:700px">1.99</span>
  <p class="bev" style="left:598px;top:690px">16 oz Bottled Tea<br>Home-Brewed Iced Tea<br>20 oz Bottles (Fizzo Cola, Diet Fizzo, Orange,<br>Ginger Ale, Citrus Peak, Barrel Root Beer)</p>
  <span class="bev-price" style="left:482px;top:753px">2.99</span>
  <span class="bev-price" style="left:730px;top:753px">2.99</span>
  <p class="bev" style="left:598px;top:741px">2 Liter Bottles (Fizzo Cola, Diet Fizzo, Orange,<br>Ginger Ale, Citrus Peak, Barrel Root Beer)</p>
  <p class="bev" style="left:598px;top:772px">16 oz Bottled Water</p>
  <span class="bev-price" style="left:598px;top:791px">1.59</span>

  <!-- Right column -->
  <div class="ornament" role="img" aria-label="Decorative scroll flourish" style="left:926px;top:18px;width:124px;height:20px;background:linear-gradient(90deg,rgba(181,122,94,.15),rgba(139,26,14,.35),rgba(181,122,94,.15))"></div>
  <h2 class="section-title" style="left:986px;top:72px">GHILDRENS MENU</h2>
  <div class="small-table" style="left:830px;top:113px;width:149px">
    <div class="r"><span>Cheeseburger and Fries</span><span>5.99</span></div>
    <div class="r"><span>Chicken Fingers and Fries</span><span>6.59</span></div>
    <div class="r"><span>Grilled Cheese and Fries</span><span>5.99</span></div>
    <div class="r"><span>Grilled Chicken Breast</span><span></span></div>
    <div class="r"><span>with Buttered Pasta</span><span>6.99</span></div>
  </div>
  <div class="small-table" style="left:1002px;top:113px;width:149px">
    <div class="r"><span>Linguini and Meatball</span><span>6.99</span></div>
    <div class="r"><span>Mac and Cheese</span><span>4.99</span></div>
    <div class="r"><span>Mini Pizza</span><span>5.99</span></div>
    <div class="r"><span>Ravioli and Meatball</span><span>6.99</span></div>
    <div class="r"><span>Sliders (2) and Fries</span><span>5.99</span></div>
  </div>

  <h2 class="section-title" style="left:989px;top:246px">AWESOME BURGERS</h2>
  <div class="rule" style="left:838px;top:278px;width:136px"></div>
  <div class="rule" style="left:1006px;top:278px;width:144px"></div>

  <div class="item col-right" style="top:307px"><span class="item-name">Cheese Burger</span><span class="item-price">7.99</span></div>
  <div class="item col-right" style="top:339px"><span class="item-name">Bacon Cheddar</span><span class="item-price">8.99</span></div>
  <p class="item-desc col-right" style="top:362px">Applewood smoked bacon, sharp cheddar</p>
  <div class="item col-right" style="top:397px"><span class="item-name">Blue Cheese BLT</span><span class="item-price">9.59</span></div>
  <p class="item-desc col-right" style="top:420px">Bacon, lettuce, tomato, onion, mayonnaise, bleu cheese</p>
  <div class="item col-right" style="top:452px"><span class="item-name">California</span><span class="item-price">9.99</span></div>
  <p class="item-desc col-right" style="top:475px">Avocado, roasted green chilies, pepper jack cheese, chipotle<br>mayo, ranch dressing</p>
  <div class="band" style="left:802px;top:508px;width:364px">
    <div class="item" style="left:27px;width:322px"><span class="item-name">Gourment Sliders</span><span class="item-price">8.99</span></div>
  </div>
  <p class="item-desc col-right" style="top:546px">5 bite-sized burgers with American cheese on mini potato rolls</p>
  <div class="item col-right" style="top:585px"><span class="item-name">Mushroom Swiss</span><span class="item-price">8.59</span></div>
  <p class="item-desc col-right" style="top:609px">Sautéed mushrooms, onions and mayo topped with Swiss cheese</p>
  <div class="item col-right" style="top:637px"><span class="item-name">Portabella</span><span class="item-price">8.59</span></div>
  <p class="item-desc col-right" style="top:658px">Angus burger, roasted portabella, melted provolone cheese</p>
  <div class="item col-right" style="top:687px"><span class="item-name">Pub</span><span class="item-price">9.99</span></div>
  <p class="item-desc col-right" style="top:713px">Crown Steak sauce and mayo, topped with onion rings, bleu cheese</p>
  <div class="item col-right" style="top:749px"><span class="item-name">Smokehouse Barbecue</span><span class="item-price">9.99</span></div>
  <p class="item-desc col-right" style="top:774px">Smoked bacon, melted cheddar cheese, crispy onion strings,<br>tangy barbecue-ranch sauce</p>
</main>
</body>
</html>
```